Lantern Motion for Neighbors Business Cards

I need business cards for staff in a new startup. Our company name is Movrela - we train Tai Chi teachers. But our biggest project is called Lantern Motion for Neighbors - a federal project to put together free Tai Chi classes for Vets all across America. It's a young company, with a spirit of excitement, passion, a desire to do good for others (our Vets) and a modern style and sensibility. In other words, not old-fashioned Asian martial arts theme, but something new.

Industry/Entity Type

Health And Wellness

Contact Information for Business Card

The topic is ancient healing, but the company is the Pembrooks - so I'd like a card design that captures that.

Font styles to use
Sans Serif

Colors

Designer to choose colors to be used in the design.

Requirements
Nice to have
• I've got two logos - one for the company and one for the project. I want to see if we can incorporate them both without it becoming too busy.
Should not have
• Overly old-fashioned yin-yang themes.

```html
<!DOCTYPE html>
<html lang="en">
<head>
<meta charset="UTF-8">
<title>Lantern Motion for Neighbors — Business Card</title>
<link rel="stylesheet" href="https://fonts.googleapis.com/css2?family=Open+Sans:wght@400&family=Roboto+Condensed:wght@400&display=swap">
<style>
  :root {
    --page-bg: #f1f2f2;
    --navy: #2a2d5c;
    --navy-soft: #41426e;
    --navy-faint: #35376a;
    --paper: #ffffff;
    --ink: #2a2d5c;
    --brand-red: #c8102e;
    --on-navy: #ffffff;
  }
  * { box-sizing: border-box; margin: 0; padding: 0; }
  html, body {
    width: 1200px; height: 1200px; overflow: hidden;
    background: var(--page-bg);
  }
  .canvas { position: relative; width: 1200px; height: 1200px; }

  .card {
    position: absolute;
    left: 285px;
    width: 628px;
    height: 358px;
    overflow: hidden;
  }
  .card--front { top: 189px; background: var(--navy); }
  .card--back  { top: 623px; background: var(--paper); }

  /* Front */
  .backdrop-disc {
    position: absolute;
    left: 243px; top: -80px;
    width: 340px; height: 340px;
    border-radius: 50%;
    background: var(--navy-soft);
  }
  .backdrop-name {
    position: absolute;
    left: 110px; top: 232px;
    font-family: "Open Sans", sans-serif;
    font-weight: 400;
    font-size: 110px;
    line-height: 1;
    color: var(--navy-faint);
    white-space: nowrap;
    transform: rotate(-8deg);
    transform-origin: left top;
  }
  .project-mark {
    position: absolute;
    left: 27px; top: 24px;
    display: flex; align-items: center; gap: 12px;
  }
  .project-mark__circle {
    width: 62px; height: 62px;
    border: 2px solid var(--on-navy);
    border-radius: 50%;
  }
  .project-mark__name {
    font-family: "Open Sans", sans-serif;
    font-weight: 400;
    font-size: 17px;
    color: var(--on-navy);
    letter-spacing: 0.5px;
  }

  /* Back */
  .contact {
    position: absolute;
    left: 211px; top: 101px;
    font-family: "Roboto Condensed", sans-serif;
    font-weight: 400;
    color: var(--ink);
  }
  .contact__address { font-size: 19.5px; line-height: 25px; }
  .contact__reach { margin-top: 21px; font-size: 17.5px; line-height: 23px; }

  .company-mark {
    position: absolute;
    left: 488px; top: 250px;
    display: flex; align-items: center; gap: 8px;
  }
  .company-mark__circle {
    width: 46px; height: 46px;
    border-radius: 50%;
    background: var(--brand-red);
  }
  .company-mark__name {
    font-family: "Roboto Condensed", sans-serif;
    font-weight: 400;
    font-size: 22px;
    color: var(--brand-red);
  }
</style>
</head>
<body>
<main class="canvas">
  <section class="card card--front" aria-label="Card front">
    <div class="backdrop-disc" aria-hidden="true"></div>
    <div class="backdrop-name" aria-hidden="true">Movrela</div>
    <div class="project-mark">
      <span class="project-mark__circle" aria-hidden="true"></span>
      <span class="project-mark__name">Lantern Motion for Neighbors</span>
    </div>
  </section>

  <section class="card card--back" aria-label="Card back">
    <div class="contact">
      <p class="contact__address">Dana Whitfield<br>1187&nbsp; Harbor Crest Lane<br>Lexford OH, 44120</p>
      <p class="contact__reach">614-555-0187<br>dwhitfield@movrela.com</p>
    </div>
    <div class="company-mark">
      <span class="company-mark__circle" aria-hidden="true"></span>
      <span class="company-mark__name">Movrela</span>
    </div>
  </section>
</main>
</body>
</html>
```